PDF-Dokumente für Vermietung und Verwaltung von Immobilien
Zielgruppe
TornWerk, Vermietung und Verwaltung von Immoblien
Aufgabenstellung
Wir haben ganz viele Dokumente, die als PDF erstellt werden sollen, Einheitlich im CI Design, mit Logo etc. Manche PDFS müssen ausfüllbar sein andere sind einfach nur zum Drucken. es sind ca 10-20 Word/PDF Dokumente.

```html
<!DOCTYPE html>
<html lang="de">
<head>
<meta charset="utf-8">
<title>Fragenbogen zur Immobilienbewertung – TornWerk</title>
<link href="https://fonts.googleapis.com/css2?family=Open+Sans:wght@400;600&family=Source+Sans+3:wght@400;600&family=Tinos&display=swap" rel="stylesheet">
<style>
  :root {
    --navy: #1f2e4a;
    --line: #26365a;
    --text: #1f2e4a;
    --muted: #4a4f57;
    --paper: #ffffff;
  }
  * { box-sizing: border-box; margin: 0; padding: 0; }
  html, body { width: 849px; height: 1200px; overflow: hidden; background: var(--paper); }
  .sheet { position: relative; width: 849px; height: 1200px; background: var(--paper); color: var(--text); font-family: "Source Sans 3", Arial, sans-serif; }

  .title-top, .title-main { position: absolute; background: var(--navy); color: #fff; font-family: "Open Sans", Arial, sans-serif; }
  .title-top { left: 71px; top: 57px; width: 215px; height: 37px; font-size: 21px; padding: 11px 0 0 16px; letter-spacing: .5px; }
  .title-main { left: 71px; top: 93px; width: 345px; height: 43px; font-size: 21.5px; font-weight: 600; letter-spacing: 2.6px; padding: 8px 0 0 14px; }

  .brand { position: absolute; right: 55px; top: 108px; font-family: "Open Sans", Arial, sans-serif; font-size: 22px; font-weight: 600; color: var(--navy); }

  .field { position: absolute; border: 1.5px solid var(--line); }
  .field-label { position: absolute; left: 6px; top: 4px; font-size: 12.8px; color: var(--text); }
  .field-note { position: absolute; font-size: 9px; line-height: 1.35; color: var(--text); }

  .opt { position: absolute; display: flex; align-items: center; gap: 8px; font-size: 10.4px; line-height: 1.3; color: var(--text); white-space: nowrap; }
  .cb { width: 16px; height: 16px; border: 1px solid var(--line); flex: none; background: #fff; }
  .opt.top { align-items: flex-end; }

  .spec { position: absolute; width: 232px; font-size: 8.6px; line-height: 1.42; color: var(--text); }

  .inline-label { position: absolute; font-size: 10.4px; color: var(--text); }

  .footer-rule { position: absolute; left: 39px; top: 1090px; width: 771px; height: 2px; background: var(--navy); }
  .footer-col { position: absolute; top: 1101px; font-family: "Tinos", serif; font-size: 11.4px; line-height: 15px; color: var(--muted); }
  .footer-col .row { display: flex; align-items: center; gap: 4px; }
  .footer-col .ico { width: 9px; height: 9px; flex: none; }
  .footer-col .indent { padding-left: 13px; }

  .footer-band { position: absolute; left: 0; top: 1176px; width: 849px; height: 24px; }
</style>
</head>
<body>
<main class="sheet">

  <div class="title-top">Fragenbogen zur</div>
  <div class="title-main">IMMOBILIENBEWERTUNG</div>

  <div class="brand">TornWerk</div>

  <div class="field" style="left:71px;top:170px;width:237px;height:33px"><span class="field-label">Vorname</span></div>
  <div class="field" style="left:315px;top:170px;width:236px;height:33px"><span class="field-label">Nachname</span></div>
  <div class="field" style="left:558px;top:170px;width:236px;height:33px"></div>

  <div class="field" style="left:71px;top:210px;width:237px;height:34px"><span class="field-label">Telefon</span></div>
  <div class="field" style="left:315px;top:210px;width:479px;height:34px"><span class="field-label">E-Mail-Adresse</span></div>

  <div class="field" style="left:71px;top:250px;width:723px;height:34px"><span class="field-label">Objektadresse</span></div>

  <div class="opt" style="left:78px;top:297px"><span class="cb"></span><span>freistehendes<br>Einfamilienhaus</span></div>
  <div class="opt" style="left:200px;top:301px"><span class="cb"></span><span>2-Familienhaus</span></div>
  <div class="opt" style="left:316px;top:301px"><span class="cb"></span><span>Doppelhaushälfte</span></div>
  <div class="opt" style="left:448px;top:301px"><span class="cb"></span><span>Reihenmittelhaus</span></div>
  <div class="opt" style="left:574px;top:301px"><span class="cb"></span><span>Reihenendhaus</span></div>

  <div class="opt" style="left:78px;top:346px"><span class="cb"></span><span>Eigentumswohnung</span></div>
  <div class="opt" style="left:200px;top:346px"><span class="cb"></span><span>Mehrfamilienhaus</span></div>
  <div class="field" style="left:315px;top:337px;width:236px;height:40px"><span class="field-label">Anzahl Wohneinheiten</span></div>
  <div class="field" style="left:558px;top:337px;width:236px;height:40px">
    <span class="field-label">Miteigentum</span>
    <span class="field-label" style="top:21px">Anteil</span>
    <span class="field-label" style="top:21px;left:97px">von</span>
  </div>

  <div class="field" style="left:71px;top:384px;width:237px;height:34px"><span class="field-label">Baujahr</span></div>
  <div class="field" style="left:315px;top:384px;width:236px;height:34px"><span class="field-label">Wohnfläche</span></div>
  <div class="field" style="left:558px;top:384px;width:236px;height:34px"><span class="field-label">Grundstücksfläche</span></div>

  <div class="field" style="left:71px;top:425px;width:723px;height:93px"><span class="field-label">Modernisierung</span></div>
  <div class="opt" style="left:78px;top:448px"><span class="cb"></span><span>Kernsanierung im Jahr:</span></div>
  <div class="inline-label" style="left:322px;top:451px"><b>oder</b> (Falls eine Teilmodernisierung durchgeführt wurde, kreuzen Sie bitte Zutreffendes an.)</div>
  <div class="opt" style="left:78px;top:473px"><span class="cb"></span><span>Dach im Jahr:</span></div>
  <div class="opt" style="left:322px;top:473px"><span class="cb"></span><span>Leitungen im Jahr:</span></div>
  <div class="opt" style="left:559px;top:473px"><span class="cb"></span><span>Dämmung im Jahr:</span></div>
  <div class="opt" style="left:78px;top:497px"><span class="cb"></span><span>Fenster im Jahr:</span></div>
  <div class="opt" style="left:322px;top:497px"><span class="cb"></span><span>Heizung im Jahr:</span></div>
  <div class="opt" style="left:559px;top:497px"><span class="cb"></span><span>Innen im Jahr:</span></div>

  <div class="field" style="left:71px;top:526px;width:723px;height:120px"><span class="field-label">Ausstattung</span></div>
  <div class="opt" style="left:78px;top:549px"><span class="cb"></span><span>einfach</span></div>
  <div class="opt" style="left:322px;top:549px"><span class="cb"></span><span>mittel</span></div>
  <div class="opt" style="left:559px;top:549px"><span class="cb"></span><span>gehoben</span></div>
  <p class="spec" style="left:78px;top:570px">Mauerwerk mit Putz und Anstrich, Holzfenster mit Einfachverglasung, einfach Betondachpfannen und keine Wärmedämmung, einfaches Bad mit WC, eine elektrische Speicherheizung sowie ein Boiler für Warmwasser</p>
  <p class="spec" style="left:322px;top:570px">Wärmedämmputz, mittlerer Wärmedämmstandard, Kunststofffenster, Rollladen und Isolierverglasung, Betondachpfannen sowie eine mittlere Wärmedämmung, 1 Bad mit Dusche und Badewanne sowie ein Gäste-WC, eine Zentralheizung</p>
  <p class="spec" style="left:559px;top:570px">Verblendmauerwerk, Aluminiumfenster, elektr. Rollladen, Wärmeschutz- und/oder Schallschutzverglasung, hoher Wärmedämmstandard, Tondachpfannen oder Schieferdeckung, Dachausbauten, 1-2 großzügige Bäder sowie ein Gäste-WC, Zentralheizung mit Flachheizkörpern oder Fußbodenheizung, Klimaanlagen, Solaranlagen</p>

  <div class="field" style="left:71px;top:653px;width:723px;height:56px"><span class="field-label">Dachausbau</span></div>
  <div class="opt" style="left:78px;top:685px"><span class="cb"></span><span>nicht bekannt</span></div>
  <div class="opt" style="left:192px;top:685px"><span class="cb"></span><span>nicht ausgebaut</span></div>
  <div class="opt" style="left:316px;top:685px"><span class="cb"></span><span>Flachdach</span></div>
  <div class="opt top" style="left:412px;top:677px"><span class="cb"></span><span>ausgebautes<br>Dachgeschoss</span></div>
  <div class="opt top" style="left:528px;top:677px"><span class="cb"></span><span>ausgebauter<br>Spitzboden</span></div>
  <div class="opt top" style="left:636px;top:677px"><span class="cb"></span><span>ausgebautes<br>Dach u. Spitzboden</span></div>

  <div class="field" style="left:72px;top:716px;width:358px;height:43px"><span class="field-label">Anzahl Geschosse</span></div>
  <p class="field-note" style="left:268px;top:724px">Das (ausgebaute) Dachgeschoss wird<br>nicht als volles Geschoss gerechnet.</p>
  <div class="field" style="left:436px;top:716px;width:358px;height:43px"><span class="field-label">Unterkellert</span></div>
  <div class="opt" style="left:443px;top:738px"><span class="cb"></span><span>nicht</span></div>
  <div class="opt" style="left:528px;top:738px"><span class="cb"></span><span>zum Teil</span></div>
  <div class="opt" style="left:636px;top:738px"><span class="cb"></span><span>voll</span></div>

  <div class="field" style="left:72px;top:767px;width:358px;height:43px"><span class="field-label">Gesamtzustand des Hauses</span></div>
  <div class="opt" style="left:78px;top:790px"><span class="cb"></span><span>gut</span></div>
  <div class="opt" style="left:148px;top:790px"><span class="cb"></span><span>mittel</span></div>
  <div class="opt" style="left:233px;top:790px"><span class="cb"></span><span>mäßig</span></div>
  <div class="field" style="left:436px;top:767px;width:358px;height:43px">
    <span class="field-label">Anzahl Garagen</span>
    <span class="field-label" style="left:168px">Anzahl Stellplätze</span>
  </div>

  <div class="field" style="left:72px;top:817px;width:479px;height:46px"><span class="field-label">Erbbaurecht</span></div>
  <div class="opt" style="left:78px;top:843px"><span class="cb"></span><span>nein</span></div>
  <div class="opt" style="left:148px;top:843px"><span class="cb"></span><span>ja</span></div>
  <div class="opt" style="left:207px;top:843px"><span class="cb"></span><span>Bes. Vorbehalte&nbsp; Beginn (Jahr):</span></div>
  <div class="inline-label" style="left:415px;top:847px">Vertragsablaufjahr:</div>
  <div class="field" style="left:558px;top:817px;width:236px;height:46px"><span class="field-label">Erbbauzins p.a.</span></div>

  <div class="field" style="left:72px;top:871px;width:358px;height:69px"><span class="field-label">Besonderheiten im Grundbuch</span></div>
  <div class="opt" style="left:78px;top:895px"><span class="cb"></span><span>Wohnrechte</span></div>
  <div class="opt" style="left:207px;top:895px"><span class="cb"></span><span>Wege und Leitungsrechte</span></div>
  <div class="opt" style="left:78px;top:918px"><span class="cb"></span><span>Nießbrauchrechte</span></div>
  <div class="opt" style="left:207px;top:918px"><span class="cb"></span><span>keine</span></div>
  <div class="field" style="left:436px;top:871px;width:358px;height:69px"><span class="field-label">Mieteinnahmen</span></div>
  <div class="opt" style="left:443px;top:895px"><span class="cb"></span><span>nein</span></div>
  <div class="opt" style="left:528px;top:895px"><span class="cb"></span><span>ja, Kaltmiete pro Monat:</span></div>

  <div class="field" style="left:72px;top:948px;width:722px;height:75px"><span class="field-label">Notizen/Hinweise</span></div>

  <div class="field" style="left:72px;top:1030px;width:358px;height:41px"><span class="field-label">Anzahl Objektbilder</span></div>
  <div class="inline-label" style="left:303px;top:1037px">(Fotos bitte beschriften.)</div>
  <div class="field" style="left:436px;top:1030px;width:358px;height:41px"><span class="field-label">Unterschrift</span></div>

  <div class="footer-rule"></div>

  <div class="footer-col" style="left:44px">
    <div class="row"><svg class="ico" viewBox="0 0 10 10"><path d="M5 0.5a3.3 3.3 0 0 0-3.3 3.3C1.7 6.3 5 9.5 5 9.5s3.3-3.2 3.3-5.7A3.3 3.3 0 0 0 5 .5zm0 4.6a1.3 1.3 0 1 1 0-2.6 1.3 1.3 0 0 1 0 2.6z" fill="#1f2e4a"/></svg><span>TornWerk GmbH</span></div>
    <div class="indent">Am Mühlenfeld 16</div>
    <div class="indent">28195 Weserstadt</div>
  </div>

  <div class="footer-col" style="left:231px">
    <div class="row"><svg class="ico" viewBox="0 0 10 10"><path d="M2.2 1l1.6 1.7-.8 1.3a6 6 0 0 0 3 3l1.3-.8L9 7.8 8 9C4.5 9 1 5.5 1 2z" fill="#1f2e4a"/></svg><span>0421 55501234</span></div>
    <div class="row"><svg class="ico" viewBox="0 0 10 10"><rect x="0.8" y="2" width="8.4" height="6" fill="none" stroke="#1f2e4a" stroke-width="1"/><path d="M1 2.3l4 3 4-3" fill="none" stroke="#1f2e4a" stroke-width="1"/></svg><span>info@tornwerk.de</span></div>
    <div class="row"><svg class="ico" viewBox="0 0 10 10"><circle cx="5" cy="5" r="4" fill="none" stroke="#1f2e4a"/><ellipse cx="5" cy="5" rx="1.8" ry="4" fill="none" stroke="#1f2e4a" stroke-width=".8"/><path d="M1 5h8" stroke="#1f2e4a" stroke-width=".8"/></svg><span>www.tornwerk.de</span></div>
  </div>

  <div class="footer-col" style="left:395px">
    <div class="row"><svg class="ico" viewBox="0 0 10 10"><path d="M5 .5L9.5 3H.5z" fill="#1f2e4a"/><rect x="1.5" y="3.8" width="1.3" height="4" fill="#1f2e4a"/><rect x="4.35" y="3.8" width="1.3" height="4" fill="#1f2e4a"/><rect x="7.2" y="3.8" width="1.3" height="4" fill="#1f2e4a"/><rect x=".5" y="8.3" width="9" height="1.2" fill="#1f2e4a"/></svg><span>Bankverbindung:</span></div>
    <div class="indent">Sparkasse Nordheide Beispiel</div>
    <div class="indent">IBAN: DE00 1234 5678 9012 3456 78</div>
    <div class="indent">BIC.: SPKXDE21XXX</div>
  </div>

  <div class="footer-col" style="left:655px">
    <div class="row"><svg class="ico" viewBox="0 0 10 10"><circle cx="5" cy="3" r="2.3" fill="#1f2e4a"/><path d="M.8 9.6c0-2.5 1.9-4 4.2-4s4.2 1.5 4.2 4z" fill="#1f2e4a"/></svg><span>Geschäftsführer:</span></div>
    <div class="indent">Jonas Berger &amp; Lea Hartmann</div>
    <div class="row"><svg class="ico" viewBox="0 0 10 10"><rect x="1.5" y=".5" width="7" height="9" fill="none" stroke="#1f2e4a"/><path d="M3 3h4M3 5h4M3 7h3" stroke="#1f2e4a" stroke-width=".8"/></svg><span>USt-ID-Nr.: DE123456789</span></div>
    <div class="indent">HRB 12345 HB</div>
  </div>

  <svg class="footer-band" viewBox="0 0 849 24" preserveAspectRatio="none" aria-hidden="true">
    <rect width="849" height="24" fill="#1f2e4a"/>
    <polygon points="648,24 652,24 659,0 655,0" fill="#ffffff"/>
  </svg>

</main>
</body>
</html>
```